Like Donuts and Coffee Some Things are Just Better Together Fold Over Postcard

My name is Dora Kimball and I AM the marketing and sales department of a small B2B software sales company. Since 1983 PVR Software Solutions was worked with small to medium sized cities and utility companies. We sell and support BrookLedger Fund Accounting, BrookLedger Payroll and the interfacing KLT Tessera utility billing software. Many of our customers use both software products. We are a very customer support oriented company working together with our clients to make their job easier.
Updates

Thank you so much for your designs...i'm just getting back from long holiday weekend so plan to get on it today so you should all hear something from me soon!

Target Market(s)

Small cities and town and utility companies in United States. Primary target at city is city clerk or city treasurer, usually females but not always.

Industry/Entity Type

Business Software

Font styles to use
Other font styles liked:
• Calibri

Requirements
Must have
• Postcard is first of several to be designed. This particular postcard will be my first contact with prospects in a campaign called "Better Together" where I use different pairs of items that go together. I tend to think food but open to any options (like little boys and mud puddles). Wanting Two sided fold over postcard with ability to run through printer to print address. I send these out about 20 a week and just run them through my printer. I try to stay with our colors of Tan $179 G164 B147 and Red 128 and medium gray
Should not have
• I prefer very simple that isn't too busy. My second page is pushing "busy" but I don't know how to simplify it.. hopefully you will have wonderful ideas!

```html
<!DOCTYPE html>
<html lang="en">
<head>
<meta charset="utf-8">
<title>Better Together Postcard</title>
<link rel="stylesheet" href="https://fonts.googleapis.com/css2?family=Carlito:ital,wght@0,400;0,700;1,400&family=Oswald:wght@500;600&family=Dancing+Script:wght@700&display=swap">
<style>
  :root {
    --red: #c1272d;
    --tan: #b3a493;
    --tan-light: #d9cfc3;
    --gray: #6d6e71;
    --gray-light: #e6e6e6;
    --ink: #3a3a3a;
    --white: #ffffff;
  }
  * { box-sizing: border-box; margin: 0; padding: 0; }
  html, body { width: 900px; height: 1200px; overflow: hidden; background: var(--white); }
  body { position: relative; font-family: "Carlito", Calibri, sans-serif; color: var(--ink); }

  .card { position: absolute; left: 54px; width: 792px; background: var(--white); box-shadow: 0 2px 8px rgba(0,0,0,.25); overflow: hidden; }

  /* Front */
  .front { top: 40px; height: 530px; }
  .front-photo { position: absolute; inset: 0 0 110px 0;
    background: linear-gradient(180deg, #f6f6f6 0%, #e4e0dc 60%, #c9b9a8 100%); }
  .front-lead { position: absolute; left: 70px; top: 70px; font-size: 36px; color: var(--red); }
  .front-script { position: absolute; right: 60px; top: 22px; font-family: "Dancing Script", cursive; font-size: 86px; line-height: .9; color: var(--red); text-align: center; transform: rotate(-4deg); }
  .front-footer { position: absolute; left: 0; right: 0; bottom: 0; height: 110px; display: flex; border-top: 4px solid var(--gray-light); }
  .brand { display: flex; align-items: center; gap: 10px; }
  .brand-mark { width: 22px; height: 22px; border-radius: 50%; background: var(--red); flex: none; }
  .brand-name { font-weight: 700; color: var(--gray); white-space: nowrap; }
  .front-footer .brand { width: 300px; padding-left: 30px; }
  .front-footer .brand-name { font-size: 24px; }
  .tagline { flex: 1; background: var(--red); color: var(--white); padding: 26px 22px; }
  .tagline-title { font-family: "Oswald", sans-serif; font-weight: 600; font-size: 21px; line-height: 1.15; white-space: nowrap; }
  .tagline-sub { font-size: 17px; margin-top: 4px; white-space: nowrap; }

  /* Back */
  .back { top: 600px; height: 560px; }
  .back-title { font-family: "Oswald", sans-serif; font-weight: 600; font-size: 30px; line-height: 1.3; color: var(--red); text-align: center; margin-top: 10px; }
  .back-intro { font-size: 15px; font-weight: 700; text-align: center; width: 620px; margin: 2px auto 0; line-height: 1.3; }
  .products { display: flex; margin-top: 12px; height: 214px; }
  .product { flex: 1; padding: 10px 20px; font-size: 12.5px; line-height: 1.35; }
  .product.fund { background: var(--tan-light); border-top: 4px solid var(--tan); }
  .product.billing { border-top: 4px solid var(--gray-light); }
  .product p { margin-bottom: 5px; }
  .product ul { list-style: none; }
  .product li { padding-left: 12px; position: relative; }
  .product li::before { content: ""; position: absolute; left: 0; top: 7px; width: 5px; height: 5px; background: var(--red); }
  .clients-title { font-family: "Oswald", sans-serif; font-weight: 600; font-size: 24px; line-height: 1.3; color: var(--red); text-align: center; margin-top: 6px; }
  .quotes { display: flex; gap: 30px; padding: 2px 24px 0; }
  .quote { flex: 1; font-size: 11.5px; line-height: 1.3; font-style: italic; color: var(--gray); }
  .quote cite { display: block; text-align: right; font-weight: 700; font-style: normal; color: var(--ink); margin-top: 2px; }
  .back-footer { position: absolute; left: 0; right: 0; bottom: 0; height: 64px; border-top: 4px solid var(--red); background: var(--gray-light); display: flex; align-items: center; padding: 0 24px; }
  .back-footer .brand-name { font-size: 20px; }
  .phone { font-family: "Oswald", sans-serif; font-weight: 600; font-size: 30px; color: var(--red); margin-left: 60px; }
  .address { margin-left: auto; font-size: 11.5px; text-align: right; line-height: 1.3; color: var(--gray); }
</style>
</head>
<body>

<section class="card front">
  <div class="front-photo" role="img" aria-label="Photo of a stack of chocolate chip cookies beside a glass of milk"></div>
  <p class="front-lead">Something are just ...</p>
  <p class="front-script">Better<br>Together</p>
  <div class="front-footer">
    <div class="brand"><span class="brand-mark"></span><span class="brand-name">PVR Software Solutions</span></div>
    <div class="tagline">
      <p class="tagline-title">INCREDIBLE SOFTWARE &amp; EXCEPTIONAL SUPPORT</p>
      <p class="tagline-sub">For Your Municipal Accounting, Payroll and Utility Billing Needs</p>
    </div>
  </div>
</section>

<section class="card back">
  <h1 class="back-title">WORKING BETTER TOGETHER!</h1>
  <p class="back-intro">Since 1983, PVR Software Solutions has partnered with small to medium sized cities and utility companies. Our main goal is to provide our clients with incredible software that best meets their accounting and utility billing needs.</p>

  <div class="products">
    <div class="product fund">
      <p>BrookLedger Fund Accounting is an affordable, comprehensive fund accounting and payroll solution designed specifically for municipals with small to medium size populations.</p>
      <ul>
        <li>GASB Recommended Format</li>
        <li>Customizable Annual Financial Statement</li>
        <li>Budget by Individual Fund and Department within the Funds</li>
        <li>LOTS of Reports – Customizable to Your Needs</li>
        <li>BrookLedger Payroll – Payroll that Saves You Both Time and Money</li>
        <li>Interfaces with KLT Tessera Utility Billing System</li>
        <li>Exceptional Support Team – Working together for your success!!</li>
      </ul>
    </div>
    <div class="product billing">
      <p>KLT Tessera Utility Billing Software includes all the features that thousands of utility billing customers have come to expect. Here are a few:</p>
      <ul>
        <li>High Control Folder Lists</li>
        <li>Unlimited Transaction History</li>
        <li>Unlimited Rate Spaces</li>
        <li>Complete Rate Analysis</li>
        <li>CASS Certification Available</li>
        <li>LOTS of Report Options</li>
        <li>Exceptional Support Team – Working together for your success!!</li>
      </ul>
    </div>
  </div>

  <h2 class="clients-title">OUR CLIENT</h2>
  <div class="quotes">
    <blockquote class="quote">"We have found BrookLedger to be very user friendly and the support that PVR has provided has made it very easy to use. There is a comfort in knowing that the staff at PVR is just a phone call away from helping you solve your problem."<cite>Janet R., City of Elm Ridge</cite></blockquote>
    <blockquote class="quote">"KLT is the simplest billing software any utility company could use. The staff is always there to help; they are always pleasant and patient. We would recommend KLT to any billing company in the market for a quality upgrade."<cite>Marla P., Cedar Hollow Water Assn.</cite></blockquote>
  </div>

  <div class="back-footer">
    <div class="brand"><span class="brand-mark"></span><span class="brand-name">PVR Software Solutions</span></div>
    <p class="phone">800.555.0142</p>
    <p class="address">1450 Harbor Ridge Blvd, Springdale, AR 72764<br>Tel: (501) 555-0187 · Fax: (501) 555-0188<br>info@pvrsoftware.example · www.pvrsoftware.example</p>
  </div>
</section>

</body>
</html>
```